Seed Oil Safety Card for Healthy Restaurant Dining

I am seeking a design for a physical card to communicate my wife's health-related dietary restriction regarding seed oils. This card will be given to restaurant waiters to ensure her meals are prepared without seed oils, as it is a health issue and not merely a preference.
My wife cannot eat any “seed oil” or “processed oil”, including:
- Vegetable oil
- Canola oil
- Soybean oil
- Sunflower oil
- Corn oil
- Cottonseed oil
- Safflower oil
- Peanut oil
- Sesame oil
Oils that are OK for her to consume:
- Butter (most preferable)
- Extra virgin olive oil
- Avocado oil
- Coconut oil
- Ghee
- Lard
- Any other animal-based fats
Key Design Requirements:
- Clarity and speed of communication: The card should be easily read and understood by waiters, even in low-light environments, emphasizing that it's a health concern.
- Avoid common misconceptions: Ensure the design doesn't imply common dietary preferences like "vegetarian" or "no butter." Animal fats and butter are actually preferable for her!
- Preferred term: Use "seed oils" as the term to describe what she cannot eat due to her health issue.
- Trace amounts are acceptable: Communicate that it's OK to use cookware that has previously been in contact with seed oils, but not to have seed oil as an ingredient. Please suggest a concise way to convey this.
- Card dimensions: Design should be 3.5” x 2.25” (standard credit-card size on cardlomex.example). Horizontal or vertical layouts are both fine, whichever makes the message clearer.
Design Suggestions:
- Utilize bold and easy-to-read typography to communicate the main message.
- Consider incorporating relevant icons or graphics that help convey the message without adding confusion.
- Use contrasting colors to enhance readability, especially in low-light situations.
- To communicate the “trace amounts OK” part, consider phrases such as:
- "Cross-contamination acceptable"
- “Used cookware OK, no ingredient use”
- “Separate cookware not necessary”
Thank you for your assistance in creating this essential card for my wife's health and safety when dining out!

```html
<!DOCTYPE html>
<html lang="en">
<head>
<meta charset="utf-8">
<title>Food Restriction Card</title>
<link href="https://fonts.googleapis.com/css2?family=Exo+2:ital,wght@0,300;0,400;0,700;1,800&display=swap" rel="stylesheet">
<style>
  :root {
    --page: #ffffff;
    --card: #ffffff;
    --card-edge: #c9c9c9;
    --title-red: #e8000b;
    --no-red: #d10000;
    --ok-green: #00b505;
    --warn-orange: #f5a100;
    --ink: #1a1a1a;
    --on-color: #ffffff;
    --photo-light: #eceae4;
    --photo-gold: #e6b43a;
    --photo-amber: #c98a12;
  }
  * { margin: 0; padding: 0; box-sizing: border-box; }
  html, body { width: 849px; height: 1200px; overflow: hidden; background: var(--page); }
  body { font-family: "Exo 2", sans-serif; position: relative; }

  .card {
    position: absolute;
    left: 144px;
    width: 560px;
    height: 360px;
    border-radius: 18px;
    overflow: hidden;
  }
  .card--front { top: 30px; background: var(--card); border: 1.5px solid var(--card-edge); }
  .card--back { top: 420px; }

  .card-title {
    position: absolute;
    left: 0; right: 0;
    text-align: center;
    font-weight: 800;
    font-style: italic;
    color: var(--title-red);
    letter-spacing: 0.5px;
  }
  .card--front .card-title { top: 40px; font-size: 31px; }

  .oil-group { position: absolute; top: 88px; width: 187px; }
  .oil-group--no { left: 76px; }
  .oil-group--ok { left: 297px; }
  .oil-heading { font-size: 23px; font-weight: 300; color: var(--ink); line-height: 1; padding-left: 1px; }
  .oil-status { font-size: 13.5px; font-weight: 700; line-height: 1.2; margin-top: 2px; letter-spacing: 0.4px; }
  .oil-group--no .oil-status { color: var(--no-red); }
  .oil-group--ok .oil-status { color: var(--ok-green); }

  .oil-box {
    position: relative;
    height: 152px;
    clip-path: polygon(0 0, 100% 0, 100% calc(100% - 22px), calc(100% - 22px) 100%, 0 100%);
  }
  .oil-group--no .oil-box { background: var(--no-red); }
  .oil-group--ok .oil-box { background: var(--ok-green); }

  .oil-list {
    list-style: none;
    position: absolute;
    left: 16px;
    color: var(--on-color);
    font-size: 11.5px;
    font-weight: 300;
    line-height: 14.3px;
  }
  .oil-group--no .oil-list { top: 12px; }
  .oil-group--ok .oil-list { top: 25px; }
  .oil-list li::before { content: "- "; }

  .oil-icon { position: absolute; }
  .oil-group--no .oil-icon { left: 140px; top: 58px; }
  .oil-group--ok .oil-icon { left: 122px; top: 56px; }

  .trace-note {
    position: absolute;
    left: 76px;
    top: 310px;
    display: flex;
    align-items: center;
    gap: 10px;
    color: var(--warn-orange);
    font-size: 14px;
    font-weight: 700;
    letter-spacing: 0.5px;
  }

  .back-photo {
    position: absolute;
    inset: 0;
    background:
      radial-gradient(ellipse 120px 170px at 250px 140px, var(--photo-gold), transparent 70%),
      radial-gradient(ellipse 150px 60px at 270px 330px, var(--photo-gold), transparent 70%),
      radial-gradient(ellipse 70px 140px at 520px 260px, #f1e6a6, transparent 70%),
      radial-gradient(ellipse 80px 90px at 40px 40px, var(--photo-amber), transparent 70%),
      linear-gradient(135deg, var(--photo-light), #f6f4ee 60%, var(--photo-light));
  }
  .back-band {
    position: absolute;
    left: 0; right: 0;
    top: 141px;
    height: 77px;
    background: rgba(255, 255, 255, 0.78);
  }
  .card--back .card-title { top: 156px; font-size: 36px; }
</style>
</head>
<body>

<section class="card card--front" aria-label="Food restriction card, front">
  <h1 class="card-title">FOOD RESTRICTION CARD</h1>

  <div class="oil-group oil-group--no">
    <h2 class="oil-heading">Processed Oil</h2>
    <p class="oil-status">Not Allowed</p>
    <div class="oil-box">
      <ul class="oil-list">
        <li>Vegetable oil</li>
        <li>Canola oil</li>
        <li>Soybean oil</li>
        <li>Sunflower oil</li>
        <li>Corn oil</li>
        <li>Cottonseed oil</li>
        <li>Safflower oil</li>
        <li>Peanut oil</li>
        <li>Sesame oil</li>
      </ul>
      <svg class="oil-icon" width="18" height="50" viewBox="0 0 18 50" fill="none" stroke="#fff" stroke-width="1.6" aria-hidden="true">
        <rect x="6" y="1" width="6" height="5"/>
        <path d="M6 6 L3 12 V48 H15 V12 L12 6 Z"/>
        <path d="M9 18 c-2 3 -2 5 0 5 c2 0 2 -2 0 -5z"/>
        <line x1="3" y1="28" x2="15" y2="28"/>
        <line x1="3" y1="32" x2="15" y2="32"/>
        <line x1="3" y1="36" x2="15" y2="36"/>
        <line x1="3" y1="40" x2="15" y2="40"/>
        <line x1="3" y1="44" x2="15" y2="44"/>
      </svg>
    </div>
  </div>

  <div class="oil-group oil-group--ok">
    <h2 class="oil-heading">Natural Oil</h2>
    <p class="oil-status">Allowed</p>
    <div class="oil-box">
      <ul class="oil-list">
        <li>Butter (most preferable)</li>
        <li>Extra virgin olive oil</li>
        <li>Avocado oil</li>
        <li>Coconut oil</li>
        <li>Ghee</li>
        <li>Lard</li>
        <li>Animal-based fats</li>
      </ul>
      <svg class="oil-icon" width="44" height="50" viewBox="0 0 44 50" fill="none" stroke="#fff" stroke-width="1.6" aria-hidden="true">
        <rect x="30" y="2" width="6" height="5"/>
        <path d="M28 7 H38 V12 L41 16 V48 H26 V16 L28 12 Z"/>
        <rect x="29" y="24" width="9" height="16"/>
        <ellipse cx="12" cy="38" rx="10" ry="8"/>
        <ellipse cx="12" cy="38" rx="6" ry="4.5"/>
        <path d="M6 33 L18 43"/>
        <path d="M14 22 c-3 3 -3 6 0 6 c3 0 3 -3 0 -6z"/>
        <path d="M20 18 c-2 2 -2 4 0 4 c2 0 2 -2 0 -4z"/>
      </svg>
    </div>
  </div>

  <p class="trace-note">
    <svg width="19" height="17" viewBox="0 0 19 17" fill="none" stroke="#f5a100" stroke-width="1.3" aria-hidden="true">
      <path d="M9.5 1 L18 16 H1 Z" stroke-linejoin="round"/>
      <line x1="9.5" y1="6" x2="9.5" y2="11"/>
      <circle cx="9.5" cy="13.3" r="0.7" fill="#f5a100"/>
    </svg>
    Cross-contamination acceptable
  </p>
</section>

<section class="card card--back" aria-label="Food restriction card, back">
  <div class="back-photo" role="img" aria-label="Photo of bottles of yellow cooking oil lying on a light surface"></div>
  <div class="back-band"></div>
  <h1 class="card-title">FOOD RESTRICTION CARD</h1>
</section>

</body>
</html>
```